Tumble Nest - mobile play centre poster designs

Who are we - we are a mobile playground business that specialises in providing entertainment to children in a safe, clean environment either at home or in a function centre. Brief - create 4 different signs to be displayed on our playgrounds. Please find attached 3 photos from our competitors to use as a guide. Corflute sign - size A1 Toddler zone - size A1 Playground rules - size A4 No climbing - size 20cmx8cm sending through photos and documents now.
Colors
Designer to choose colors to be used in the design.
Requirements
Must have
- Colour, be very specific with the rules, pictures

```html
<!DOCTYPE html>
<html lang="en">
<head>
<meta charset="utf-8">
<title>Tumble Nest – Playground Rules</title>
<link rel="stylesheet" href="https://fonts.googleapis.com/css2?family=Anton&family=Source+Sans+3:wght@600;700&family=Montserrat:wght@500&display=swap">
<style>
  :root {
    --yellow: #f4d21c;
    --yellow-light: #fbe55a;
    --bamboo: #5f9a2a;
    --bamboo-dark: #3f6f1a;
    --panel-top: #ffffff;
    --panel-bottom: #f6efc4;
    --green-text: #1f6b2a;
    --orange: #f08a1d;
    --grey-text: #5d5d5d;
    --foliage-light: #7fae3a;
    --foliage-dark: #2d5e1c;
  }
  * { box-sizing: border-box; margin: 0; padding: 0; }
  html, body { width: 950px; height: 1200px; overflow: hidden; background: #ffffff; }
  .poster {
    position: relative;
    width: 950px;
    height: 1200px;
    overflow: hidden;
    background: repeating-linear-gradient(180deg, var(--yellow) 0 58px, var(--yellow-light) 58px 90px);
    font-family: "Source Sans 3", sans-serif;
  }
  .bamboo-frame {
    position: absolute;
    left: 44px; top: 36px;
    width: 862px; height: 1126px;
    border: 12px solid var(--bamboo);
    outline: 2px solid var(--bamboo-dark);
    outline-offset: -7px;
  }
  .panel {
    position: absolute;
    left: 70px; top: 52px;
    width: 817px; height: 1080px;
    background: linear-gradient(180deg, var(--panel-top) 0%, #fdfbe9 35%, var(--panel-bottom) 100%);
    box-shadow: 0 0 8px rgba(0,0,0,0.25);
  }
  .brand {
    position: absolute;
    top: 18px; left: 0; width: 100%;
    display: flex; justify-content: center; align-items: center; gap: 22px;
  }
  .brand-name {
    font-weight: 700;
    font-size: 78px;
    line-height: 100px;
    color: var(--orange);
    letter-spacing: 1px;
  }
  .brand-dot {
    width: 44px; height: 44px; border-radius: 50%;
    background: var(--bamboo);
  }
  .tagline {
    position: absolute;
    top: 124px; left: 0; width: 100%;
    text-align: center;
    font-family: "Montserrat", sans-serif;
    font-weight: 500;
    font-size: 34px;
    line-height: 44px;
    letter-spacing: 2px;
    color: var(--grey-text);
  }
  .supervision {
    position: absolute;
    top: 228px; left: 0; width: 100%;
    text-align: center;
    font-weight: 700;
    font-size: 29px;
    line-height: 38px;
    color: var(--green-text);
  }
  .rules-title {
    position: absolute;
    top: 334px; left: 0; width: 100%;
    text-align: center;
    font-family: "Anton", sans-serif;
    font-weight: 400;
    font-size: 84px;
    line-height: 104px;
    letter-spacing: -3px;
    color: var(--orange);
    text-shadow: 3px 4px 4px rgba(0,0,0,0.35);
  }
  .rules {
    position: absolute;
    top: 486px; left: 50px;
    list-style: none;
  }
  .rule {
    display: flex; align-items: center;
    height: 75px;
  }
  .rule-icon {
    width: 78px; height: 62px;
    border-radius: 12px;
    margin-right: 60px;
  }
  .rule-no {
    font-family: "Anton", sans-serif;
    font-size: 56px;
    line-height: 1;
    color: var(--orange);
    width: 74px;
  }
  .rule-text {
    font-weight: 700;
    font-size: 37px;
    color: var(--green-text);
  }
  .icon-shoes { background: linear-gradient(135deg, #4f8a4a, #cfd8cf); }
  .icon-net { background: linear-gradient(135deg, #555, #c9543a); }
  .icon-food { background: linear-gradient(135deg, #e03a2a, #f2b632); }
  .icon-bottle { background: linear-gradient(135deg, #7ab6e6, #dcecf8); }
  .icon-gum { background: linear-gradient(135deg, #a66a3a, #f4a7c0); }
  .icon-sharp { background: linear-gradient(135deg, #1e3e4a, #c9a27a); }
  .icon-paint { background: linear-gradient(135deg, #f2b04a, #4cb87a); }
  .foliage {
    position: absolute;
    left: 50px; top: 1074px;
    width: 850px; height: 126px;
    border-radius: 60px 60px 0 0;
    background: linear-gradient(180deg, var(--foliage-light) 0%, var(--foliage-dark) 100%);
  }
</style>
</head>
<body>
<main class="poster">
  <div class="bamboo-frame"></div>
  <section class="panel">
    <div class="brand">
      <span class="brand-name">Tumble Nest</span>
      <span class="brand-dot"></span>
    </div>
    <p class="tagline">MOBILE PLAY CENTRE</p>
    <p class="supervision">Parents/Guardians must supervise children using<br>this play equipment at all times</p>
    <h1 class="rules-title">PLAY GROUND RULES</h1>
    <ul class="rules">
      <li class="rule"><span class="rule-icon icon-shoes" role="img" aria-label="Illustration of a pair of sneakers"></span><span class="rule-no">NO</span><span class="rule-text">shoes – socks must be worn</span></li>
      <li class="rule"><span class="rule-icon icon-net" role="img" aria-label="Illustration of a child climbing a net"></span><span class="rule-no">NO</span><span class="rule-text">climbing the nets</span></li>
      <li class="rule"><span class="rule-icon icon-food" role="img" aria-label="Illustration of fries, a burger and a drink"></span><span class="rule-no">NO</span><span class="rule-text">food or drink</span></li>
      <li class="rule"><span class="rule-icon icon-bottle" role="img" aria-label="Illustration of a water bottle and a glass"></span><span class="rule-no">NO</span><span class="rule-text">bottle or glass</span></li>
      <li class="rule"><span class="rule-icon icon-gum" role="img" aria-label="Illustration of a child blowing a bubble of gum"></span><span class="rule-no">NO</span><span class="rule-text">chewing gum</span></li>
      <li class="rule"><span class="rule-icon icon-sharp" role="img" aria-label="Illustration of cutlery and a sharp object"></span><span class="rule-no">NO</span><span class="rule-text">sharp objects</span></li>
      <li class="rule"><span class="rule-icon icon-paint" role="img" aria-label="Illustration of a child with face paint"></span><span class="rule-no">NO</span><span class="rule-text">face painting</span></li>
    </ul>
  </section>
  <div class="foliage" role="img" aria-label="Row of green jungle plants along the bottom edge"></div>
</main>
</body>
</html>
```